Flyer-Design für Business Center
Zielgruppe
Wir sind Co-Working /Business Center Anbieter auf Basis eines Mitgliedschaft Konzeptes. Bei uns kann man Arbeitsplätze und Büroräume mit Kaffee und Wasser in einer Lounge anmieten. Dazu bieten wir Bedarfsgerechte Mitgliedschaften an. Unsere Kunden sind Kreative, Programmierer, Freiberufler aber auch größere Unternehmen.
Aufgabenstellung
DIN LANG A 4, der Flyer wird gedruckt und kommt in Aussteller. Er soll als Eye Catcher den Preis ab 69,90 für 4 Wochen beinhalten. In diesem Preis ist alles inclusive. Also Wasser, Kaffee, Cappuccino, Drucker, Kopierer, Möbel, Putzfrau, Schreibtisch. Bürostuhl. Gleichzeitig soll der Flyer auch als PDF versendet werden können.
Weitere Information findet man auf unserer Webseite www.kranichfeldwerk.com

```html
<!DOCTYPE html>
<html lang="de">
<head>
<meta charset="utf-8">
<title>Kranichfeld Werk – Co-Working &amp; Business Center Flyer</title>
<link rel="stylesheet" href="https://fonts.googleapis.com/css2?family=Open+Sans:wght@400;600&display=swap">
<style>
  :root {
    --brand-blue: #29a8e0;
    --brand-blue-dark: #1f8fc8;
    --text-blue: #2a9ad6;
    --text-muted: #4d7391;
    --white: #ffffff;
    --stage: #e6f1f8;
    --photo-warm: #b59a83;
    --photo-cool: #8f98a3;
  }
  * { box-sizing: border-box; margin: 0; padding: 0; }
  html, body {
    width: 1040px; height: 1200px; overflow: hidden;
    background: var(--stage);
    font-family: "Open Sans", Arial, sans-serif;
  }
  .flyer {
    position: absolute; left: 240px; top: 40px;
    width: 560px; height: 1120px;
    background: var(--white);
    box-shadow: 0 10px 30px rgba(20, 70, 110, 0.18);
    overflow: hidden;
  }
  .header {
    position: absolute; left: 0; top: 0; width: 100%; height: 160px;
    display: flex; align-items: center;
  }
  .brand {
    position: absolute; left: 44px; top: 58px;
    display: flex; align-items: center; gap: 10px;
    color: var(--text-blue); font-weight: 400; font-size: 24px; line-height: 1.1;
  }
  .brand-dot { width: 14px; height: 14px; border-radius: 50%; background: var(--text-blue); flex: none; }
  .header-title {
    position: absolute; left: 281px; top: 72px;
    color: var(--text-blue); font-weight: 600; font-size: 27px; line-height: 33px;
  }
  .tagline-band {
    position: absolute; left: 0; top: 160px; width: 100%; height: 152px;
    background: var(--brand-blue);
    display: flex; align-items: center; justify-content: center;
    color: var(--white); font-weight: 600; font-size: 20px;
  }
  .photo {
    position: absolute; left: 0; top: 312px; width: 100%; height: 374px;
    background: linear-gradient(160deg, #d9dde0 0%, var(--photo-cool) 35%, var(--photo-warm) 75%, #6e5a4c 100%);
  }
  .photo-strip {
    position: absolute; left: 0; top: 686px; width: 100%; height: 29px;
    background: var(--brand-blue);
  }
  .price-badge {
    position: absolute; left: 325px; top: 556px;
    width: 212px; height: 212px; border-radius: 50%;
    background: var(--white); border: 2px solid var(--brand-blue);
    display: flex; align-items: center; justify-content: center;
  }
  .price-core {
    width: 190px; height: 190px; border-radius: 50%;
    background: var(--brand-blue); color: var(--white);
    position: relative;
  }
  .price-from { position: absolute; left: 36px; top: 96px; font-size: 20px; }
  .price-amount { position: absolute; left: 60px; top: 50px; font-size: 60px; font-weight: 400; letter-spacing: -1px; }
  .price-period { position: absolute; right: 30px; top: 124px; font-size: 20px; font-weight: 600; }
  .benefits { position: absolute; left: 50px; top: 735px; }
  .benefits-title { color: var(--text-blue); font-weight: 600; font-size: 22px; margin-bottom: 14px; }
  .benefit-list { list-style: none; }
  .benefit {
    display: flex; align-items: center; gap: 12px;
    color: var(--text-muted); font-weight: 600; font-size: 20px;
    height: 41.5px;
  }
  .benefit svg { width: 20px; height: 20px; flex: none; }
  .footer-band {
    position: absolute; left: 0; top: 967px; width: 100%; height: 153px;
    background: var(--brand-blue);
    display: flex; align-items: center; justify-content: center;
    color: var(--white); font-weight: 600; font-size: 20px;
  }
</style>
</head>
<body>
  <article class="flyer">
    <header class="header">
      <div class="brand"><span class="brand-dot"></span><span>Kranichfeld<br>Werk</span></div>
      <h1 class="header-title">Co-Working &amp;<br>Business Center</h1>
    </header>

    <section class="tagline-band">Moderne, effiziente und günstige Büroräume</section>

    <div class="photo" role="img" aria-label="Helle Business-Lounge mit Sesseln, Sofa, Bartheke und Fensterfront mit Blick auf die Stadt"></div>
    <div class="photo-strip"></div>

    <div class="price-badge">
      <div class="price-core">
        <span class="price-from">ab</span>
        <span class="price-amount">69€</span>
        <span class="price-period">p.M.</span>
      </div>
    </div>

    <section class="benefits">
      <h2 class="benefits-title">Deine Vorteile:</h2>
      <ul class="benefit-list">
        <li class="benefit">
          <svg viewBox="0 0 20 20" fill="none" stroke="#4d7391" stroke-width="2"><rect x="5" y="2" width="10" height="5"/><rect x="2" y="7" width="16" height="7" fill="#4d7391"/><rect x="5" y="12" width="10" height="6" fill="#fff"/></svg>
          Drucker / Kopierer
        </li>
        <li class="benefit">
          <svg viewBox="0 0 22 20" fill="#4d7391"><circle cx="11" cy="6" r="3.5"/><circle cx="4.5" cy="7" r="2.5"/><circle cx="17.5" cy="7" r="2.5"/><path d="M5 18c0-4 2.5-7 6-7s6 3 6 7z"/><path d="M0 17c0-3 1.8-5 4.5-5 1 0 1.5.3 1.5.3C4.8 13.6 4 15.3 4 17z"/><path d="M22 17c0-3-1.8-5-4.5-5-1 0-1.5.3-1.5.3 1.2 1.3 2 3 2 4.7z"/></svg>
          Reinigungsservice
        </li>
        <li class="benefit">
          <svg viewBox="0 0 20 20" fill="none" stroke="#4d7391" stroke-width="1.8"><path d="M10 4H3v13h13v-7"/><path d="M8 12l1-3 7-7 2 2-7 7z"/></svg>
          Schreibtisch / Möbel / Bürostuhl
        </li>
        <li class="benefit">
          <svg viewBox="0 0 20 20" fill="none" stroke="#4d7391" stroke-width="1.8"><path d="M10 17S2 12 2 7a4 4 0 0 1 8-1 4 4 0 0 1 8 1c0 5-8 10-8 10z"/></svg>
          Wasser / Kaffee / Cappuccino
        </li>
      </ul>
    </section>

    <footer class="footer-band">Berlin - Bonn - Monheim am Rhein - Frankfurt</footer>
  </article>
</body>
</html>
```